Equipment Finance Specialist I work with companies who need the funds to buy their equipment

I would like a business card that stands out on the shelves. I want to be able to hand it to someone and say WOW. This card should have my logo.
You can put color into it I am very open on design and color

What my company does is we deal with dealerships that sell equipment such as Dump Trucks garbage trucks tractors trailers. Customers get referred to us and depending on their time in business we will ask for the following items

Companies that have been in business for more than two years we have a credit application program up to 250K . With this program we need the following items Credit application filled out(which is what I would like to be able for the customer to click on my website to get.) as well as three current month bank statements.

Deals over 250k we will need the following items

2 years business tax returns
2 years personal tax returns
Profit & Loss statement
Personal Financial Statement

what we do
100% FINANCING
SEASONAL PAYMENTS
LOAN BALLOON PAYMENTS
TRAC LEASING
LOW-INTEREST REFINANCING RATES
DEBT CONSOLIDATION

We specialize in creative financing solutions and offer a variety of reliable, flexible and expandable lending choices.

Target Market(s)

Trucking Companies

Industry/Entity Type

Trucking Company

Contact Information for Business Card

* $250,000 Application only Program
* Loans from $30,000 to 5,000,000
* Competitive Interest Rates

Font styles to use
Serif
Sans Serif

Colors

Designer to choose colors to be used in the design.

Requirements
Must have
• On the back of the card.
• * $250,000 Application only Program
• * Loans from $30,000 to 5,000,000
• My name, email, website. address
• * Competitive Interest Rates
• * 100% Financing
Nice to have
• I want my logo to pop on the card
• My logo is the great one I would like to use
Should not have
• I am up for your creativity as well

```html
<!DOCTYPE html>
<html lang="en">
<head>
<meta charset="UTF-8">
<title>Ridgeline Funding – Business Card</title>
<link href="https://fonts.googleapis.com/css2?family=Roboto+Condensed:wght@400;700&family=Roboto:wght@400;500&display=swap" rel="stylesheet">
<style>
  :root {
    --backdrop: #2a2a2c;
    --card: #141415;
    --silver: #b4b4b6;
    --silver-dim: #8e8e90;
    --ink-light: #e2e2e2;
    --rule: #5a5a5c;
  }
  * { margin: 0; padding: 0; box-sizing: border-box; }
  html, body { width: 1200px; height: 900px; overflow: hidden; }
  body {
    background: var(--backdrop);
    font-family: "Roboto", Arial, sans-serif;
    display: flex;
    flex-direction: column;
    align-items: center;
    justify-content: center;
    gap: 40px;
  }
  .card {
    width: 630px;
    height: 360px;
    background: var(--card);
    border-radius: 4px;
    box-shadow: 0 12px 30px rgba(0,0,0,0.45);
    position: relative;
  }
  /* Front */
  .card-front {
    display: flex;
    align-items: center;
    justify-content: center;
  }
  .brand {
    display: flex;
    align-items: center;
    gap: 18px;
  }
  .brand-dot {
    width: 70px; height: 70px;
    border-radius: 50%;
    background: var(--silver);
  }
  .brand-name {
    font-family: "Roboto Condensed", Arial, sans-serif;
    font-weight: 700;
    font-size: 46px;
    letter-spacing: 2px;
    text-transform: uppercase;
    color: var(--silver);
    line-height: 1;
  }
  /* Back */
  .card-back { padding: 0 40px; }
  .identity-row {
    position: absolute;
    top: 92px; left: 0; right: 0;
    display: flex;
    justify-content: center;
    align-items: flex-start;
  }
  .person {
    text-align: right;
    padding-right: 30px;
    padding-top: 18px;
  }
  .person-name {
    font-family: "Roboto Condensed", Arial, sans-serif;
    font-weight: 700;
    font-size: 36px;
    color: var(--silver);
    letter-spacing: 1px;
    line-height: 1;
  }
  .person-title {
    font-family: "Roboto Condensed", Arial, sans-serif;
    font-size: 17px;
    color: var(--silver-dim);
    letter-spacing: 1px;
    margin-top: 6px;
  }
  .divider {
    width: 1px;
    height: 150px;
    background: var(--rule);
  }
  .contact {
    padding-left: 26px;
    color: var(--ink-light);
    font-size: 15px;
    line-height: 1.35;
  }
  .address { margin-bottom: 14px; }
  .contact-line {
    display: flex;
    align-items: center;
    gap: 10px;
  }
  .contact-line svg { width: 13px; height: 13px; flex: none; fill: var(--silver); }
  .offers {
    position: absolute;
    left: 0; right: 0; bottom: 48px;
    text-align: center;
    color: var(--silver-dim);
    font-size: 16px;
    line-height: 1.4;
  }
  .offers .sep { margin: 0 6px; }
</style>
</head>
<body>
  <section class="card card-front">
    <div class="brand">
      <span class="brand-dot"></span>
      <span class="brand-name">Ridgeline Funding</span>
    </div>
  </section>

  <section class="card card-back">
    <div class="identity-row">
      <div class="person">
        <div class="person-name">DANIEL REYES</div>
        <div class="person-title">CEO/FOUNDER</div>
      </div>
      <div class="divider"></div>
      <div class="contact">
        <div class="address">4120 Harbor View Road<br>Juneau, Alaska 99801</div>
        <div class="contact-line">
          <svg viewBox="0 0 24 24"><path d="M6.6 10.8a15.1 15.1 0 0 0 6.6 6.6l2.2-2.2c.3-.3.7-.4 1-.2 1.1.4 2.3.6 3.6.6.6 0 1 .4 1 1V20c0 .6-.4 1-1 1A17 17 0 0 1 3 4c0-.6.4-1 1-1h3.5c.6 0 1 .4 1 1 0 1.3.2 2.5.6 3.6.1.3 0 .7-.2 1z"/></svg>
          <span>555 214 7730</span>
        </div>
        <div class="contact-line">
          <svg viewBox="0 0 24 24"><path d="M2 5h20v14H2z M2 5l10 8 10-8" stroke="#141415" stroke-width="1.6"/></svg>
          <span>daniel@ridgelinefunding.com</span>
        </div>
        <div class="contact-line">
          <svg viewBox="0 0 24 24"><circle cx="12" cy="12" r="10"/><path d="M2 12h20M12 2c3 3 3 17 0 20M12 2c-3 3-3 17 0 20" stroke="#141415" stroke-width="1.5" fill="none"/></svg>
          <span>www.ridgelinefunding.com</span>
        </div>
      </div>
    </div>
    <div class="offers">
      <div>$250,000 Application only Program<span class="sep">•</span>Loans from $30,000 to 5,000,000</div>
      <div>Competitive Interest Rates<span class="sep">•</span>100% Financing</div>
    </div>
  </section>
</body>
</html>
```